Outdoor Billboard on PVC (double sides)

Hello, i need special design for billboard which is located 15 meters away from the main road. Measures form Billboard: 8 meters X 2 meters. I need Billboard for Window tinting. I have one picture (white Porsche) which you can use as a main BIG Picture- or you have better idea i am so open to your suggestions. Billboard has to be shocking ... i want to make it look like this is similiar way from style. I have a lot of pictures from my cars which i have done in my garage which we can use it. I dont know if you can use this ... quality? On the billboard so it blames be turn left in 30Meter. My logo wants bi attached- please use it on black background. text which schould be down on the Billboard: Proffesionale Tint my logo VELTANA put somewhere where looks cool Phone: 0664 2915 807 E-mail: marlow.veltana@brisknet.example Website: www. veltana-glasdunkel.at

Target Market(s)

This billboard wants to be on the border between two countrys..i have my garage company here on the border- where ia am making window. A lot of cars are driving each day nearby so I want that people see this and so they look at where they have left to my garage.

Colors

Designer to choose colors to be used in the design.

Requirements
Must have
• Billboard schould have a BiG picture from white Porsche with my logo on the side and text Proffesional scarf tint. Down on the board it schould be info Tel, email, website. This measures 8x2 meters

```html
<!DOCTYPE html>
<html lang="de">
<head>
<meta charset="utf-8">
<title>VELTANA – Billboard</title>
<link rel="stylesheet" href="https://fonts.googleapis.com/css2?family=Bebas+Neue&family=Oswald:wght@500&family=Open+Sans:wght@400;600&display=swap">
<style>
  :root {
    --red: #e4141c;
    --black: #0d0d0d;
    --white: #ffffff;
    --page: #e9ecef;
    --car-light: #eef0f3;
    --car-mid: #c9cdd3;
    --car-dark: #4a4d52;
  }
  * { box-sizing: border-box; margin: 0; padding: 0; }
  html, body { width: 1200px; height: 962px; overflow: hidden; background: var(--page); }
  .billboard {
    position: absolute; left: 30px; top: 335px;
    width: 1140px; height: 292px;
    background: var(--white); overflow: hidden;
    box-shadow: 0 6px 20px rgba(0,0,0,.15);
  }
  .headline {
    position: absolute; left: 20px;
    font-family: "Bebas Neue", sans-serif;
    font-size: 76px; line-height: 1; letter-spacing: -0.5px;
  }
  .headline--red { top: 22px; color: var(--red); }
  .headline--black { top: 88px; color: var(--black); }
  .web-tag {
    position: absolute; left: 20px; top: 168px;
    height: 34px; padding: 0 10px;
    background: var(--black); color: var(--white);
    font-family: "Oswald", sans-serif; font-weight: 500;
    font-size: 20px; line-height: 34px; letter-spacing: 0.6px;
  }
  .red-rule {
    position: absolute; left: 0; top: 224px; width: 100%; height: 5px;
    background: var(--red);
  }
  .info-band {
    position: absolute; left: 0; top: 229px; width: 100%; height: 63px;
    background: var(--black);
  }
  .direction {
    position: absolute; left: 20px; top: 17px;
    display: flex; align-items: center; gap: 12px;
    color: var(--white);
    font-family: "Oswald", sans-serif; font-weight: 500;
    font-size: 24px; letter-spacing: 1.2px; line-height: 1;
  }
  .contacts {
    position: absolute; right: 22px; top: 28px;
    display: flex; align-items: center; gap: 16px;
    color: var(--white);
    font-family: "Open Sans", sans-serif; font-size: 12.5px;
  }
  .contact { display: flex; align-items: center; gap: 6px; }
  .contact-icon {
    width: 11px; height: 11px; background: var(--red);
    display: inline-flex; align-items: center; justify-content: center;
  }
  .brand {
    display: flex; align-items: center; gap: 5px; margin-left: 6px;
    font-family: "Open Sans", sans-serif; font-weight: 600;
    font-size: 14px; color: var(--red); letter-spacing: 0.5px;
  }
  .brand-dot {
    width: 14px; height: 14px; border-radius: 50%;
    background: var(--red);
  }
  .car-photo {
    position: absolute; left: 438px; top: 40px;
    width: 676px; height: 214px;
    border-radius: 46% 40% 14% 14% / 70% 60% 20% 20%;
    background: linear-gradient(180deg, var(--car-light) 0%, var(--car-mid) 65%, var(--car-dark) 100%);
  }
</style>
</head>
<body>
  <main class="billboard">
    <h1 class="headline headline--red">PROFFESIONELLE</h1>
    <h2 class="headline headline--black">SCHEIBENTÖNUNG</h2>
    <p class="web-tag">www.veltana-glasdunkel.at</p>

    <div class="red-rule"></div>
    <section class="info-band">
      <p class="direction">
        <svg width="22" height="26" viewBox="0 0 22 26" aria-hidden="true"><polygon points="22,0 22,26 0,13" fill="#ffffff"/></svg>
        IN 30 METER NACH LINKS ABBIEGEN
      </p>
      <div class="contacts">
        <span class="contact">
          <span class="contact-icon"><svg width="8" height="8" viewBox="0 0 10 10" aria-hidden="true"><path d="M2 1l2 2-1 1.2a6 6 0 0 0 2.8 2.8L7 6l2 2-1.2 1.5C4.5 9 1 5.5.5 2.2z" fill="#fff"/></svg></span>
          0664 2915 807
        </span>
        <span class="contact">
          <span class="contact-icon"><svg width="8" height="6" viewBox="0 0 10 7" aria-hidden="true"><rect x=".5" y=".5" width="9" height="6" fill="none" stroke="#fff"/><path d="M.5.5L5 4 9.5.5" fill="none" stroke="#fff"/></svg></span>
          marlow.veltana@brisknet.example
        </span>
        <span class="brand"><span class="brand-dot"></span>VELTANA</span>
      </div>
    </section>

    <div class="car-photo" role="img" aria-label="Photo of a white sports coupé in side view with dark tinted windows"></div>
  </main>
</body>
</html>
```